Create Social Media design templates for Online-Education-Startup

We are an online platform for pupils who provide group courses and on demand individual tutroing lessons. Our core values are personalisation, family and success. We need a holistic social media design concept which includes nine possible layouts for Instagram posts which reflect our values and promote not only our offerings and special deals but also support in building our brand image (for example: telling company history, daily news, funny facts, getting to know the team etc.).
Additionally, we need design elements for our YouTube channel:
-Videocover
-Cover Image for the channel

Our main colour is orange (RGB-Code: 255;105;31) and additional colours white, black, and grey. For the reference have a look at our website: www.lernfolix.de.

Target Market(s)

We want to attract customers to our online tutoring courses and build a brand.

Industry/Entity Type

Education / Tutoring

Font styles to use
Sans Serif

Requirements
Must have
• Familiarize yourself with the style of our website. The designs should fit as well as possible.

```html
<!DOCTYPE html>
<html lang="de">
<head>
<meta charset="utf-8">
<title>Lernfolix – Online-Nachhilfe</title>
<link href="https://fonts.googleapis.com/css2?family=Poppins:wght@400;600;700&family=Oswald:wght@500;600;700&display=swap" rel="stylesheet">
<style>
  :root{
    --orange:#e96a2c;
    --white:#ffffff;
    --black:#0c0c0c;
    --grey:#d3d4d6;
    --photo-a:#b9b6ae;
    --photo-b:#e7e3dc;
  }
  *{margin:0;padding:0;box-sizing:border-box}
  html,body{width:1200px;height:1200px;overflow:hidden;background:var(--white)}
  .post{position:relative;width:1200px;height:1200px;background:var(--white);font-family:'Poppins',sans-serif;color:var(--black);overflow:hidden}
  .decor{position:absolute;inset:0}
  .brand{position:absolute;left:60px;top:53px;height:150px;display:flex;align-items:center;gap:30px}
  .brand-dot{width:150px;height:150px;border-radius:50%;border:12px solid var(--orange);flex:none}
  .brand-name{font-weight:700;font-size:44px;line-height:52px}
  .brand-sub{font-weight:400;font-size:41px;line-height:52px}
  .hero-band{position:absolute;left:0;top:245px;width:690px;height:339px;background:var(--orange)}
  .hero-text{position:absolute;left:53px;top:262px;color:var(--white);white-space:nowrap}
  .hero-title{font-weight:700;font-size:58px;line-height:71px}
  .hero-claim{margin-top:16px;font-size:26px;line-height:33px}
  .hero-offer{margin-top:22px;font-weight:700;font-size:26px;line-height:34px}
  .values-label{font-family:'Oswald',sans-serif;font-weight:600;font-size:24px;line-height:30px;position:absolute;transform:translateX(-50%);white-space:nowrap}
  .about{position:absolute;left:664px;top:652px;white-space:nowrap}
  .about-title{font-weight:700;font-size:42px;line-height:57px}
  .about-copy{margin-top:26px;font-size:20.5px;line-height:27.5px}
  .cta{position:absolute;left:654px;top:941px;width:481px;height:73px;border-radius:20px;background:var(--orange);color:var(--white);font-family:'Oswald',sans-serif;font-weight:500;font-size:24px;line-height:1;white-space:nowrap;display:flex;align-items:center;justify-content:center}
  .phone{position:absolute;left:654px;top:1034px;height:72px;display:flex;align-items:center;gap:13px;white-space:nowrap}
  .phone-icon{width:68px;height:68px;border-radius:50%;background:var(--orange);display:flex;align-items:center;justify-content:center;flex:none}
  .phone-number{font-family:'Oswald',sans-serif;font-weight:700;font-size:74px;line-height:1}
  .address{position:absolute;left:655px;top:1117px;height:38px;display:flex;align-items:center;gap:18px;font-size:22px;white-space:nowrap}
  .footer-bar{position:absolute;left:0;bottom:0;width:1200px;height:15px;background:var(--black)}
</style>
</head>
<body>
<main class="post">
  <svg class="decor" width="1200" height="1200" viewBox="0 0 1200 1200">
    <defs>
      <linearGradient id="photoTone" x1="0" y1="0" x2="1" y2="1">
        <stop offset="0" stop-color="var(--photo-a)"/>
        <stop offset="1" stop-color="var(--photo-b)"/>
      </linearGradient>
    </defs>
    <path d="M770 55 C 830 35, 900 40, 960 50" fill="none" stroke="var(--orange)" stroke-width="26" stroke-linecap="round"/>
    <ellipse cx="925" cy="338" rx="320" ry="290" transform="rotate(-18 925 338)" fill="var(--orange)"/>
    <ellipse cx="935" cy="330" rx="290" ry="248" transform="rotate(-18 935 330)" fill="var(--white)"/>
    <g role="img" aria-label="Foto: Nachhilfelehrerin und Schülerin schauen gemeinsam auf ein Tablet">
      <ellipse cx="940" cy="330" rx="280" ry="236" transform="rotate(-18 940 330)" fill="url(#photoTone)"/>
    </g>
    <g fill="none" stroke="var(--grey)" stroke-width="28">
      <circle cx="325" cy="751" r="111"/>
      <circle cx="175" cy="1019" r="111"/>
      <circle cx="480" cy="1019" r="111"/>
      <path d="M250 838 L205 905 M400 838 L445 905 M150 1125 Q327 1195 505 1125"/>
    </g>
    <g fill="var(--orange)">
      <circle cx="325" cy="643" r="20"/>
      <circle cx="77" cy="1073" r="20"/>
      <circle cx="574" cy="1073" r="20"/>
    </g>
    <g fill="none" stroke="var(--orange)" stroke-width="3" stroke-linecap="round" stroke-linejoin="round">
      <circle cx="325" cy="720" r="34"/>
      <circle cx="325" cy="711" r="8"/>
      <path d="M310 736 q15 -14 30 0 v4 h-30z"/>
      <path d="M175 952 l-38 32 v30 h76 v-30z"/>
      <circle cx="162" cy="990" r="6"/><circle cx="188" cy="990" r="6"/>
      <path d="M152 1012 v-10 q10 -8 20 0 v10 M178 1012 v-10 q10 -8 20 0 v10"/>
      <path d="M467 950 h26 v12 q0 18 -13 22 q-13 -4 -13 -22z M480 984 v12 M470 998 h20"/>
      <path d="M452 1010 l22 -12 M505 955 l4 6 l6 2 l-6 2 l-4 6 l-4 -6 l-6 -2 l6 -2z"/>
    </g>
  </svg>

  <header class="brand">
    <div class="brand-dot"></div>
    <div>
      <div class="brand-name">Lernfolix</div>
      <div class="brand-sub">Bildungsinstitut</div>
    </div>
  </header>

  <section class="hero-band"></section>
  <div class="hero-text">
    <h1 class="hero-title">Online-Nachhilfe<br>bei Lernfolix</h1>
    <p class="hero-claim">Gemeinsam für Deinen Abschluss!<br>persönlich. familiär. erfolgreich.</p>
    <p class="hero-offer">Kostenlose Probestunde</p>
  </div>

  <span class="values-label" style="left:325px;top:767px">Personalisation</span>
  <span class="values-label" style="left:175px;top:1045px">Family</span>
  <span class="values-label" style="left:480px;top:1045px">Success</span>

  <section class="about">
    <h2 class="about-title">Unser Sport ist<br>Online-Nachhilfe.</h2>
    <p class="about-copy">Unser Ziel ist Dein Abschluss, egal ob<br>Abi, Mittlerer-Schulabschluss oder Quali.<br>Unser Nachhilfe-Konzept ist genau,<br>was Du brauchst.</p>
  </section>

  <div class="cta">FÜR EINE KOSTENLOSE PROBESTUNDE KONTAKT</div>

  <div class="phone">
    <span class="phone-icon">
      <svg width="38" height="38" viewBox="0 0 24 24"><path d="M6.6 10.8a15 15 0 0 0 6.6 6.6l2.2-2.2c.3-.3.7-.4 1-.2 1.1.4 2.3.6 3.6.6.6 0 1 .4 1 1V20c0 .6-.4 1-1 1A17 17 0 0 1 3 4c0-.6.4-1 1-1h3.5c.6 0 1 .4 1 1 0 1.3.2 2.5.6 3.6.1.3 0 .7-.2 1z" fill="var(--white)"/></svg>
    </span>
    <span class="phone-number">089 55501234</span>
  </div>

  <div class="address">
    <svg width="38" height="38" viewBox="0 0 36 36"><circle cx="18" cy="18" r="18" fill="var(--orange)"/><path d="M18 8a7 7 0 0 0-7 7c0 5 7 12 7 12s7-7 7-12a7 7 0 0 0-7-7z" fill="var(--white)"/><circle cx="18" cy="15" r="2.6" fill="var(--orange)"/></svg>
    <span>Lindenallee 12 80331 Munich</span>
  </div>

  <div class="footer-bar"></div>
</main>
</body>
</html>
```